B7k Website Design

We need a website design, look, feel and functionality that uses a recently approved logo attached. This should be a highly professional looking website that is relatively simple, but scalable. The website should carry information about the company, links and blog posts. The look and feel of the website should be consistent with the logo colour palette, but does not have to stick to them exactly. The company provides high quality brokering and support services for multinational companies to work with international humanitarian organisations and the Meridian Accord. Where possible, the design should make the most of the concept that collective action has a greater impact, and that Compass9Reach can help make that happen. The attached text can be used as a basis for the website text.

Target Market(s)

Heads of company foundations, and humanitarian organisations, and Meridian Accord departments the promote collaboration

Number of Pages Required

3 page

Requirements
Should not have
• Photos of people in suits.
• Photos of poor African children begging for help, or smiling in gratitude for aid

```html
<!DOCTYPE html>
<html lang="en">
<head>
<meta charset="utf-8">
<title>Compass9Reach</title>
<link href="https://fonts.googleapis.com/css2?family=Lexend:wght@500;600&family=Oswald:wght@300;400&family=Poppins:wght@300;400;500&display=swap" rel="stylesheet">
<style>
:root{
  --orange:#f15a29;
  --blue:#2b3598;
  --navy:#1b237a;
  --ink:#111;
  --text:#555;
  --footer:#0e0e0e;
  --gold:#f5a000;
}
*{box-sizing:border-box;margin:0;padding:0}
html,body{width:1200px;height:4047px;overflow:hidden;background:#fff}
body{position:relative;font-family:'Poppins',sans-serif;color:var(--ink)}
.abs{position:absolute}
.h2{font-family:'Lexend',sans-serif;font-weight:500;font-size:44px;color:var(--ink);white-space:nowrap}
.para{font-size:14px;line-height:27.3px;color:var(--text);font-weight:300}
.btn-orange{background:var(--orange);color:#fff;border-radius:20px;font-size:16px;display:flex;align-items:center;justify-content:center}
/* header */
.brand{left:90px;top:22px;width:190px;text-align:center}
.brand-dot{width:60px;height:60px;border:3px solid var(--orange);border-radius:50%;margin:0 auto 8px}
.brand-name{font-size:23px;font-weight:500;color:var(--blue);line-height:1}
.phone{left:724px;top:38px;font-size:19px;display:flex;align-items:center;gap:6px}
.search{left:911px;top:33px;width:199px;height:34px;border:1px solid #999;border-radius:17px;font-size:13px;color:#666;padding:7px 18px;display:flex;justify-content:space-between;align-items:center}
.nav{top:96px;left:0;width:1200px;font-size:16px}
.nav span{position:absolute;white-space:nowrap}
/* hero */
.hero{left:0;top:162px;width:1200px;height:554px;
  background:
    radial-gradient(ellipse 240px 300px at 830px 250px,rgba(214,180,150,.55),transparent 70%),
    radial-gradient(ellipse 260px 240px at 1010px 470px,rgba(96,128,168,.75),transparent 70%),
    radial-gradient(ellipse 200px 180px at 640px 420px,rgba(120,132,145,.6),transparent 70%),
    linear-gradient(100deg,#263038 0%,#4d5a64 35%,#7b7c7b 60%,#5a6a78 85%,#3d4a56 100%)}
.hero-title{left:86px;top:360px;font-family:'Oswald',sans-serif;font-weight:400;font-size:78px;color:#fff;line-height:1;white-space:nowrap}
.hero-sub{left:86px;top:448px;font-family:'Oswald',sans-serif;font-weight:300;font-size:35px;color:#fff;white-space:nowrap}
.hero-arrow{top:525px;width:28px;height:28px;border-radius:50%;background:#222;border:1px solid #aaa;display:flex;align-items:center;justify-content:center}
/* about */
.frame{border:3px solid var(--ink)}
.photo{box-shadow:0 8px 18px rgba(0,0,0,.2)}
/* services */
.services{left:0;top:1272px;width:1200px;height:578px;
  background:
    radial-gradient(ellipse 260px 420px at 740px 200px,rgba(226,210,190,.7),transparent 70%),
    radial-gradient(ellipse 140px 260px at 770px 470px,rgba(150,170,200,.35),transparent 70%),
    linear-gradient(90deg,#e6ebf1 0%,#f6f4f0 45%,#e2e8ef 100%)}
.card{top:1488px;width:315px;height:295px;background:#fff;border:1px solid #ccc;text-align:center}
.card h3{margin-top:86px;font-family:'Lexend',sans-serif;font-weight:500;font-size:22px}
.card p{margin:18px auto 0;width:230px;font-size:14px;line-height:25px;color:var(--text);font-weight:300}
.card .more{margin:24px auto 0;width:113px;height:33px;border:1px solid #777;border-radius:17px;font-size:14px;display:flex;align-items:center;justify-content:center}
.card .more.active{background:var(--orange);border-color:var(--orange);color:#fff}
.icon{width:122px;height:122px;border-radius:50%;top:1420px;display:flex;align-items:center;justify-content:center}
.side-arrow{top:1594px;width:38px;height:38px;border-radius:50%;background:#fff;border:1px solid #ccc;display:flex;align-items:center;justify-content:center}
/* testimonials */
.testi{left:0;top:2509px;width:1200px;height:501px;background:linear-gradient(120deg,#1e2a8c 0%,#3340a0 45%,#1a2177 100%)}
.tcard{top:2692px;width:451px;height:224px;background:#fff;border-radius:4px}
.avatar{width:126px;height:126px;border-radius:50%;border:5px solid #fff;top:2741px;box-shadow:0 4px 10px rgba(0,0,0,.2)}
.quote{top:2714px}
.ttext{font-size:14px;line-height:25px;color:#777;font-weight:300;width:303px;text-align:justify}
.stars{color:var(--gold);font-size:14px;letter-spacing:1px}
.tname{color:var(--gold);font-size:17px;white-space:nowrap}
/* blog */
.bimg{top:3206px;height:171px}
.tag{top:3393px;height:19px;display:flex;font-size:12px;color:#fff;line-height:19px}
.tag span:first-child{background:var(--blue);padding:0 12px}
.tag span:last-child{background:#222;padding:0 8px}
.btitle{top:3426px;font-size:17px;color:#222;white-space:nowrap}
.btext{top:3459px;font-size:12px;line-height:20px;color:#777;width:315px}
.bmore{top:3500px;font-size:12px;color:var(--orange)}
/* footer */
.fline{left:0;top:3602px;width:1200px;height:9px;background:var(--blue)}
.footer{left:0;top:3611px;width:1200px;height:436px;background:var(--footer);color:#fff}
.fhead{top:3696px;font-size:20px;color:#fff;font-weight:400}
.flinks{top:3752px;font-size:15px;line-height:33px;color:#fff}
.field{left:798px;width:309px;height:34px;background:#fff;color:#555;font-size:14px;padding:7px 16px}
.send{left:798px;top:3875px;width:126px;height:36px;background:var(--orange);color:#fff;font-size:17px;display:flex;align-items:center;justify-content:center}
.bottom{left:0;top:3977px;width:1200px;height:70px;background:#050505;color:#bbb;font-size:13px;text-align:center;padding-top:32px}
</style>
</head>
<body>

<header>
  <div class="abs brand"><div class="brand-dot"></div><div class="brand-name">Compass9Reach</div></div>
  <div class="abs phone">
    <svg width="16" height="16" viewBox="0 0 24 24"><path fill="#f15a29" d="M6.6 10.8a15 15 0 006.6 6.6l2.2-2.2c.3-.3.7-.4 1-.2 1.1.4 2.3.6 3.6.6.6 0 1 .4 1 1V20c0 .6-.4 1-1 1A17 17 0 013 4c0-.6.4-1 1-1h3.5c.6 0 1 .4 1 1 0 1.3.2 2.5.6 3.6.1.3 0 .7-.2 1z"/></svg>
    1-800-555-0142
  </div>
  <div class="abs search"><span>Search</span>
    <svg width="14" height="14" viewBox="0 0 24 24"><circle cx="10" cy="10" r="6" fill="none" stroke="#222" stroke-width="3"/><path d="M15 15l6 6" stroke="#222" stroke-width="3"/></svg>
  </div>
  <nav class="abs nav">
    <span style="left:435px;color:var(--orange)">Home</span>
    <span style="left:517px">About B7k</span>
    <span style="left:628px">Founder</span>
    <span style="left:734px">Services</span>
    <span style="left:836px">Strategy</span>
    <span style="left:939px">Blog</span>
    <span style="left:1012px">Contact us</span>
  </nav>
</header>

<section>
  <div class="abs hero" role="img" aria-label="Smiling colleagues seated around a meeting table in a bright office"></div>
  <h1 class="abs hero-title" style="font-weight:400">Compass 9 reach</h1>
  <div class="abs hero-sub">Neque porro quisquam est qui dolorem</div>
  <div class="abs hero-arrow" style="left:88px"><svg width="10" height="10" viewBox="0 0 10 10"><path d="M6.5 1.5L3 5l3.5 3.5" fill="none" stroke="#fff" stroke-width="1.5"/></svg></div>
  <div class="abs hero-arrow" style="left:123px"><svg width="10" height="10" viewBox="0 0 10 10"><path d="M3.5 1.5L7 5 3.5 8.5" fill="none" stroke="#fff" stroke-width="1.5"/></svg></div>
</section>

<section>
  <div class="abs frame" style="left:90px;top:839px;width:410px;height:311px"></div>
  <div class="abs photo" role="img" aria-label="Businessman looking over a city skyline at sunset" style="left:118px;top:861px;width:397px;height:314px;background:radial-gradient(ellipse 90px 140px at 200px 110px,rgba(240,200,150,.9),transparent 70%),radial-gradient(ellipse 70px 140px at 210px 200px,rgba(70,70,80,.6),transparent 70%),linear-gradient(170deg,#6f7d8e 0%,#c8c0b2 45%,#8d96a2 75%,#5e6a78 100%)"></div>
  <h2 class="abs h2" style="left:558px;top:875px">About us</h2>
  <p class="abs para" style="left:558px;top:943px;width:531px;text-align:justify">It is a long established fact that a reader will be distracted by the readable content of a page when looking at its layout. The point of using Lorem Ipsum is that it has a more-or-less normal distribution of letters, as opposed to using 'Content here, content here', making it look like readable English. Many desk-top publishing packages and web page editors now use Lorem Ipsum as their default model text, and a search for 'lorem ipsum' will uncover many</p>
  <div class="abs btn-orange" style="left:557px;top:1121px;width:123px;height:37px">Read More</div>
</section>

<section>
  <div class="abs services" role="img" aria-label="Faded photo of a professional working at a desk"></div>
  <h2 class="abs h2" style="left:0;width:1200px;text-align:center;top:1318px">Our Services</h2>
  <div class="abs side-arrow" style="left:44px"><svg width="12" height="12" viewBox="0 0 12 12"><path d="M8 1L3 6l5 5" fill="none" stroke="#555" stroke-width="1.5"/></svg></div>
  <div class="abs side-arrow" style="left:1115px"><svg width="12" height="12" viewBox="0 0 12 12"><path d="M4 1l5 5-5 5" fill="none" stroke="#555" stroke-width="1.5"/></svg></div>

  <div class="abs card" style="left:97px"><h3>Strategy</h3><p>It is a long established fact that a reader will be distracted by the readable content of a page</p><div class="more">Read more</div></div>
  <div class="abs card" style="left:443px"><h3>Values</h3><p>It is a long established fact that a reader will be distracted by the readable content of a page</p><div class="more active">Read more</div></div>
  <div class="abs card" style="left:790px"><h3>Objective</h3><p>It is a long established fact that a reader will be distracted by the readable content of a page</p><div class="more">Read more</div></div>

  <div class="abs icon" style="left:193px;background:var(--blue)">
    <svg width="60" height="60" viewBox="0 0 60 60" fill="none" stroke="#fff" stroke-width="2"><circle cx="30" cy="14" r="6"/><circle cx="14" cy="40" r="5"/><circle cx="46" cy="40" r="5"/><path d="M6 54c0-6 4-8 8-8s8 2 8 8M38 54c0-6 4-8 8-8s8 2 8 8M14 26a18 18 0 0132 0"/></svg>
  </div>
  <div class="abs icon" style="left:537px;background:var(--orange)">
    <svg width="60" height="60" viewBox="0 0 60 60" fill="none" stroke="#fff" stroke-width="2"><rect x="12" y="8" width="30" height="42"/><path d="M18 18h18M18 26h18M18 34h12M18 42h10"/><path d="M44 22l6 6-12 12h-6v-6z"/></svg>
  </div>
  <div class="abs icon" style="left:886px;background:var(--blue)">
    <svg width="60" height="60" viewBox="0 0 60 60" fill="none" stroke="#fff" stroke-width="2"><path d="M10 24h8l18-10v32L18 36h-8z"/><path d="M14 36l4 14h6l-3-14"/><path d="M42 22l8-4M44 30h8M42 38l8 4"/></svg>
  </div>
</section>

<section>
  <h2 class="abs h2" style="left:110px;top:2067px">Founder</h2>
  <p class="abs para" style="left:110px;top:2133px;width:532px;text-align:justify">It is a long established fact that a reader will be distracted by the readable content of a page when looking at its layout. The point of using Lorem Ipsum is that it has a more-or-less normal distribution of letters, as opposed to using 'Content here, content here', making it look like readable English. Many desk-top publishing packages and web page editors now use Lorem Ipsum as their default model text, and a search for 'lorem ipsum' will uncover many</p>
  <div class="abs btn-orange" style="left:108px;top:2319px;width:124px;height:35px">Read More</div>
  <div class="abs frame" style="left:688px;top:2031px;width:410px;height:313px"></div>
  <div class="abs photo" role="img" aria-label="Founder working on a laptop in a bright office" style="left:671px;top:2053px;width:400px;height:316px;background:radial-gradient(ellipse 120px 130px at 250px 220px,rgba(120,150,190,.85),transparent 70%),radial-gradient(ellipse 60px 60px at 240px 90px,rgba(200,160,130,.7),transparent 70%),linear-gradient(150deg,#ece9e5 0%,#d4d0cb 45%,#c2c4c8 75%,#e6e4e1 100%)"></div>
</section>

<section>
  <div class="abs testi"></div>
  <h2 class="abs h2" style="left:0;width:1200px;text-align:center;top:2576px;color:#fff;font-weight:600">Testimonials</h2>

  <div class="abs tcard" style="left:124px"></div>
  <div class="abs avatar" role="img" aria-label="Portrait of a client" style="left:84px;background:radial-gradient(circle at 50% 40%,#d8c2b0 0 22%,transparent 23%),linear-gradient(#dfe3e8 0%,#cfd4da 55%,#2f3038 56%,#3a3b44 100%)"></div>
  <svg class="abs quote" style="left:492px" width="50" height="38" viewBox="0 0 50 38"><path fill="#f15a29" d="M0 38V22C0 10 6 3 18 0l2 6c-6 2-9 6-9 12h9v20zM28 38V22c0-12 6-19 18-22l2 6c-6 2-9 6-9 12h9v20z"/></svg>
  <p class="abs ttext" style="left:236px;top:2763px">The point of using Lorem Ipsum is that it has a more-or-less normal distribution of let-ters, as opposed to using 'Content</p>
  <div class="abs stars" style="left:235px;top:2853px">★★★★★</div>
  <div class="abs tname" style="left:453px;top:2852px">-&nbsp;&nbsp;&nbsp;Maren</div>

  <div class="abs tcard" style="left:647px"></div>
  <div class="abs avatar" role="img" aria-label="Portrait of a client" style="left:607px;background:radial-gradient(circle at 50% 40%,#d6b49a 0 22%,transparent 23%),linear-gradient(#6f7f8e 0%,#7d8e9c 55%,#5a8fb0 56%,#4b7fa2 100%)"></div>
  <svg class="abs quote" style="left:1015px" width="50" height="38" viewBox="0 0 50 38"><path fill="#f15a29" d="M0 38V22C0 10 6 3 18 0l2 6c-6 2-9 6-9 12h9v20zM28 38V22c0-12 6-19 18-22l2 6c-6 2-9 6-9 12h9v20z"/></svg>
  <p class="abs ttext" style="left:758px;top:2763px">The point of using Lorem Ipsum is that it has a more-or-less normal distribution of let-ters, as opposed to using 'Content</p>
  <div class="abs stars" style="left:758px;top:2853px">★★★★★</div>
  <div class="abs tname" style="left:995px;top:2852px">- Tobin</div>
</section>

<section>
  <h2 class="abs h2" style="left:0;width:1200px;text-align:center;top:3099px">Latest Blog</h2>

  <div class="abs bimg" role="img" aria-label="Woman smiling in an open-plan office" style="left:99px;width:306px;background:radial-gradient(ellipse 70px 90px at 150px 90px,rgba(110,70,50,.85),transparent 70%),linear-gradient(120deg,#e2dfdb,#bdb6ad 50%,#e8e6e3)"></div>
  <div class="abs tag" style="left:94px"><span>Dec 03</span><span>💬0</span></div>
  <div class="abs btitle" style="left:94px">Neque porro quisquam dolorem</div>
  <p class="abs btext" style="left:94px">It has survived not only five centuries, but also the leap into electronic typesetting,</p>
  <div class="abs bmore" style="left:94px">Read More »</div>

  <div class="abs bimg" role="img" aria-label="Team discussing around a table" style="left:441px;width:311px;background:radial-gradient(ellipse 120px 60px at 150px 130px,rgba(240,238,235,.8),transparent 70%),linear-gradient(120deg,#b9b2aa,#6f635a 50%,#a9a39c)"></div>
  <div class="abs tag" style="left:443px"><span>Dec 03</span><span>💬0</span></div>
  <div class="abs btitle" style="left:443px">Porro quisquam est qui</div>
  <p class="abs btext" style="left:443px">It has survived not only five centuries, but also the leap into electronic typesetting,</p>
  <div class="abs bmore" style="left:443px">Read More »</div>

  <div class="abs bimg" role="img" aria-label="Glowing digital globe network" style="left:796px;width:311px;background:radial-gradient(circle at 160px 70px,rgba(150,200,240,.7),transparent 45%),linear-gradient(120deg,#0b1f3d,#2d5b91 50%,#0d2448)"></div>
  <div class="abs tag" style="left:796px"><span>Dec 03</span><span>💬0</span></div>
  <div class="abs btitle" style="left:796px">Dolorem ipsum quia dolor</div>
  <p class="abs btext" style="left:796px">It has survived not only five centuries, but also the leap into electronic typesetting,</p>
  <div class="abs bmore" style="left:796px">Read More »</div>
</section>

<footer>
  <div class="abs fline"></div>
  <div class="abs footer"></div>
  <div class="abs fhead" style="left:94px">CONTACT US</div>
  <div class="abs fhead" style="left:364px">ABOUT</div>
  <div class="abs fhead" style="left:568px">RESOURCES</div>
  <div class="abs fhead" style="left:793px">GET IN TOUCH</div>

  <svg class="abs" style="left:94px;top:3756px" width="20" height="16" viewBox="0 0 20 16" fill="none" stroke="#fff" stroke-width="1.5"><rect x="1" y="1" width="18" height="14"/><path d="M1 1l9 8 9-8"/></svg>
  <div class="abs" style="left:122px;top:3750px;font-size:15px;color:#fff">EMAIL ADDRESS</div>
  <div class="abs" style="left:122px;top:3771px;font-size:13px;color:#fff">hello@compassreach.example</div>
  <svg class="abs" style="left:94px;top:3822px" width="20" height="20" viewBox="0 0 24 24" fill="none" stroke="#fff" stroke-width="1.5"><path d="M6.6 10.8a15 15 0 006.6 6.6l2.2-2.2c.3-.3.7-.4 1-.2 1.1.4 2.3.6 3.6.6.6 0 1 .4 1 1V20c0 .6-.4 1-1 1A17 17 0 013 4c0-.6.4-1 1-1h3.5c.6 0 1 .4 1 1 0 1.3.2 2.5.6 3.6.1.3 0 .7-.2 1z"/></svg>
  <div class="abs" style="left:122px;top:3815px;font-size:15px;color:#fff">PHONE NUMBER</div>
  <div class="abs" style="left:122px;top:3838px;font-size:13px;color:#fff">(555) 014-2290</div>

  <div class="abs flinks" style="left:364px">Home<br>About Us<br>Services<br>Products</div>
  <div class="abs flinks" style="left:569px">News<br>Support<br>Faq<br>Contact</div>

  <div class="abs field" style="top:3737px">Your Name</div>
  <div class="abs field" style="top:3781px">Email address</div>
  <div class="abs field" style="top:3824px">Phone</div>
  <div class="abs send">SEND</div>

  <div class="abs bottom">© 2018 Company Name &nbsp;All right reserved</div>
</footer>

</body>
</html>
```